Business Card Design Falcon Ridge Autos

Used car dealership, We buy, sell, trade and finance a cars.

Industry/Entity Type

Finance

Contact Information for Business Card

Falcon Ridge Autos, Buy, Sell, Trade, Finance, 418 Larkspur Ave, Millbrook, ME, 04837, 555-318-6092, www.Falcon-Ridge-Autos.example

Requirements
Must have
• Crown
Nice to have
• purple and gold colors

```html
<!DOCTYPE html>
<html lang="en">
<head>
<meta charset="utf-8">
<title>Falcon Ridge Autos – Business Card</title>
<link rel="stylesheet" href="https://fonts.googleapis.com/css2?family=EB+Garamond:wght@400&display=swap">
<style>
  :root {
    --card-cream: #fae4b4;
    --frame-blue: #2b3df5;
    --mark-gold: #f2aa00;
    --ink: #111111;
  }
  html, body {
    margin: 0;
    padding: 0;
    width: 1200px;
    height: 692px;
    overflow: hidden;
    background: var(--card-cream);
  }
  .business-card {
    position: relative;
    width: 1200px;
    height: 692px;
    box-sizing: border-box;
    border: 13px solid var(--frame-blue);
    background: var(--card-cream);
    font-family: "EB Garamond", "Garamond", Georgia, serif;
    color: var(--ink);
    font-variant-numeric: lining-nums;
  }
  .brand-mark {
    position: absolute;
    left: 527px;
    top: 52px;
  }
  .centered-line {
    position: absolute;
    left: 0;
    right: 0;
    margin: 0;
    text-align: center;
    line-height: 1;
    font-weight: 400;
    white-space: nowrap;
  }
  .company-name {
    top: 224px;
    font-size: 63px;
  }
  .services {
    top: 303px;
    font-size: 32px;
  }
  .street {
    top: 345px;
    font-size: 52px;
  }
  .city {
    top: 413px;
    font-size: 52px;
  }
  .phone,
  .website {
    position: absolute;
    top: 562px;
    margin: 0;
    font-size: 54px;
    line-height: 1;
    white-space: nowrap;
  }
  .phone { left: 34px; }
  .website { right: 34px; }
</style>
</head>
<body>
  <main class="business-card">
    <svg class="brand-mark" width="146" height="146" viewBox="0 0 146 146" role="img" aria-label="Falcon Ridge Autos brand mark">
      <circle cx="73" cy="73" r="70" fill="var(--mark-gold)" stroke="var(--frame-blue)" stroke-width="6"/>
    </svg>

    <h1 class="centered-line company-name">FALCON RIDGE AUTOS</h1>
    <p class="centered-line services">BUY, SELL, TRADE, FINANCE</p>
    <p class="centered-line street">418 Larkspur Ave.</p>
    <p class="centered-line city">Millbrook, ME 04837</p>

    <p class="phone">555-318-6092</p>
    <p class="website">Falcon-Ridge-Autos.example</p>
  </main>
</body>
</html>
```